Leaf Haven Business Card Design

My E-Commerce store is called Leaf Haven

Website address is - http://www.leafhaven-demo.com.au

I would like a colourful, friendly business with the description in the 'must haves' box incorporated into it
Updates

Please add the following to the business cards; Natural & Organic Products Online Organic Pantry Items Superfoods & Supplements Natural Skincare Eco Friendly Household Products

Industry/Entity Type

Business

Contact Information for Business Card

www.leafhaven-demo.com.au
mira@leafhaven-demo.com.au

Colors
acd037
9bcb3c
cadf82
eaf2ce

Requirements
Must have
• Natural & Organic Eco Products Online.
• Leaf Haven specialises in organic pantry items, superfoods and supplements, organic skincare for you and your family & eco friendly household products.

```html
<!DOCTYPE html>
<html lang="en">
<head>
<meta charset="utf-8">
<title>Leaf Haven Business Card</title>
<link href="https://fonts.googleapis.com/css2?family=Open+Sans:wght@400;600;700&display=swap" rel="stylesheet">
<style>
  :root {
    --backdrop: #cbcbcb;
    --card: #f5f5f5;
    --lime: #acd037;
    --lime-mid: #9bcb3c;
    --lime-pale: #cadf82;
    --lime-mist: #eaf2ce;
    --lime-ink: #6f9a1f;
    --ink: #6e6e6e;
    --ink-soft: #7c7c7c;
  }
  html, body {
    margin: 0;
    padding: 0;
    width: 1200px;
    height: 1005px;
    overflow: hidden;
    background: var(--backdrop);
    font-family: "Open Sans", sans-serif;
  }
  .canvas {
    position: relative;
    width: 1200px;
    height: 1005px;
  }
  .card {
    position: absolute;
    left: 260px;
    width: 680px;
    height: 390px;
    background: var(--card);
    box-shadow: 0 6px 14px rgba(0,0,0,0.18);
    overflow: hidden;
  }
  .card--front { top: 80px; }
  .card--back { top: 530px; }

  .brand {
    display: flex;
    align-items: center;
    gap: 14px;
    color: var(--lime-ink);
    font-weight: 600;
    white-space: nowrap;
  }
  .brand__dot {
    border-radius: 50%;
    background: var(--lime);
    flex: none;
  }

  .front-lockup {
    position: absolute;
    left: 50%;
    top: 50%;
    transform: translate(-50%, -50%);
    width: 540px;
    display: flex;
    flex-direction: column;
    align-items: center;
    text-align: center;
  }
  .card--front .brand { font-size: 54px; }
  .card--front .brand__dot { width: 40px; height: 40px; }
  .tagline {
    margin: 14px 0 0;
    padding: 4px 14px;
    background: var(--lime-mist);
    color: var(--lime-ink);
    font-size: 15px;
    font-weight: 600;
  }
  .about {
    margin: 12px 0 0;
    font-size: 13px;
    line-height: 1.5;
    color: var(--ink-soft);
  }

  .card--back .brand {
    position: absolute;
    right: 44px;
    top: 86px;
    font-size: 34px;
  }
  .card--back .brand__dot { width: 26px; height: 26px; }

  .products {
    position: absolute;
    right: 44px;
    top: 150px;
    margin: 0;
    padding: 0;
    list-style: none;
    text-align: right;
  }
  .products li {
    font-size: 13px;
    line-height: 21px;
    color: var(--ink);
  }
  .products li::after {
    content: "";
    display: inline-block;
    width: 6px;
    height: 6px;
    margin-left: 8px;
    border-radius: 50%;
    background: var(--lime-mid);
    vertical-align: middle;
  }

  .person {
    position: absolute;
    left: 52px;
    top: 82px;
  }
  .person__name {
    margin: 0;
    font-size: 25px;
    font-weight: 700;
    color: var(--ink);
    line-height: 1.1;
  }
  .person__role {
    margin: 4px 0 0 6px;
    font-size: 13px;
    color: var(--ink-soft);
  }

  .contacts {
    position: absolute;
    left: 56px;
    bottom: 62px;
    margin: 0;
    padding: 0;
    list-style: none;
  }
  .contacts li {
    display: flex;
    align-items: center;
    gap: 14px;
    font-size: 15px;
    color: var(--ink);
    line-height: 24px;
  }
  .contacts svg { width: 14px; height: 14px; flex: none; }

  .edge-band {
    position: absolute;
    left: 0;
    bottom: 0;
    width: 680px;
    height: 60px;
  }
</style>
</head>
<body>
<div class="canvas">

  <section class="card card--front" aria-label="Card front">
    <div class="front-lockup">
      <div class="brand">
        <span class="brand__dot"></span>
        <span class="brand__name">Leaf Haven</span>
      </div>
      <p class="tagline">Natural &amp; Organic Eco Products Online</p>
      <p class="about">Leaf Haven specialises in organic pantry items, superfoods and supplements, organic skincare for you and your family &amp; eco friendly household products.</p>
    </div>
  </section>

  <section class="card card--back" aria-label="Card back">
    <div class="person">
      <h1 class="person__name">Mira</h1>
      <p class="person__role">Sales Director</p>
    </div>

    <div class="brand">
      <span class="brand__dot"></span>
      <span class="brand__name">Leaf Haven</span>
    </div>

    <ul class="products">
      <li>Natural &amp; Organic Products Online</li>
      <li>Organic Pantry Items</li>
      <li>Superfoods &amp; Supplements</li>
      <li>Natural Skincare</li>
      <li>Eco Friendly Household Products</li>
    </ul>

    <ul class="contacts">
      <li>
        <svg viewBox="0 0 14 14" aria-hidden="true"><path fill="#9bcb3c" d="M1 5c0-2 2-3 6-3s6 1 6 3v1h-3V5H4v1H1zM3 7h8l1 5H2z"/><circle cx="7" cy="9.5" r="1.4" fill="#f5f5f5"/></svg>
        +00 123 456 7890
      </li>
      <li>
        <svg viewBox="0 0 14 14" aria-hidden="true"><rect x="1" y="3" width="12" height="8" fill="#9bcb3c"/><path d="M1 3l6 5 6-5" fill="none" stroke="#f5f5f5" stroke-width="1.2"/></svg>
        mira@leafhaven-demo.com.au
      </li>
      <li>
        <svg viewBox="0 0 14 14" aria-hidden="true"><circle cx="7" cy="7" r="6" fill="#9bcb3c"/><path d="M1 7h12M7 1v12M3 3.5c2.5 1.2 5.5 1.2 8 0M3 10.5c2.5-1.2 5.5-1.2 8 0" fill="none" stroke="#f5f5f5" stroke-width="0.9"/></svg>
        www.leafhaven-demo.com.au
      </li>
    </ul>

    <svg class="edge-band" viewBox="0 0 680 60" preserveAspectRatio="none" aria-hidden="true">
      <polygon points="0,46 470,30 458,60 0,60" fill="#9bcb3c"/>
      <polygon points="480,29 680,16 680,60 462,60" fill="#cadf82"/>
    </svg>
  </section>

</div>
</body>
</html>
```